■依頼の目的/概要
ビジネス本の表紙デザインをお願いします。

■本の内容
・起業初期の起業家、または副業で月収入10万円UPしたい方向けの、
77のWEBのアドバイス(テクニック)をまとめた本です。

■デザイン要望
どちらかというと、30~50代女性起業家向けです。
女性のイラストが入ると嬉しいです。

その他何かご不明な点がございましたら、お気軽にご質問下さい。
よろしくお願いいたします。

■プレセントの記載をお願いします。
①何が足りないかすぐ分かる!
WEBチェックシート

②1年で1万人フォロワーを達成した
Plumoraフォロワー増やしのコツ

③最短で成功へ向かう無料コンサル

女性らしい優しい雰囲気で、誰からも愛されるデザインと感じました。

この度はご応募頂き、誠にありがとうございました!

どのデザインも素敵で、本当に迷いました。
修正していただいた方には、親切に対応して頂き心より感謝しております。

皆様の益々のご活躍を祈念しております。
今回は本当に有難うございました。

```html
<!DOCTYPE html>
<html lang="ja">
<head>
<meta charset="utf-8">
<title>知っておくべきWEBテクニック77のポイント</title>
<link href="https://fonts.googleapis.com/css2?family=Noto+Sans+JP:wght@500;700;900&display=swap" rel="stylesheet">
<style>
  :root {
    --yellow: #f6e34c;
    --stripe: #fbf0a0;
    --ink: #1d1d1d;
    --white: #ffffff;
    --accent: #f5d23a;
    --line: #d9d9d9;
    --figure: #fff8c8;
  }
  html, body { margin: 0; padding: 0; overflow: hidden; }
  body { width: 752px; height: 1200px; font-family: "Noto Sans JP", sans-serif; color: var(--ink); }
  .cover {
    position: relative; width: 752px; height: 1200px; overflow: hidden;
    background: repeating-linear-gradient(180deg, var(--yellow) 0 8px, var(--stripe) 8px 12px);
  }
  .portrait {
    position: absolute; background: var(--figure); border-radius: 50% 50% 40% 40%;
    opacity: .85;
  }
  .p1 { left: 20px; top: 20px; width: 170px; height: 190px; }
  .p2 { left: 10px; top: 250px; width: 190px; height: 250px; }
  .p3 { left: 575px; top: 10px; width: 160px; height: 180px; }
  .p4 { left: 570px; top: 220px; width: 170px; height: 150px; }
  .p5 { left: 570px; top: 380px; width: 170px; height: 150px; }

  .tagline {
    position: absolute; left: 232px; top: -20px; width: 300px; height: 520px;
    background: var(--white); transform: rotate(-6deg);
    display: flex; justify-content: center; align-items: flex-start; padding-top: 40px;
    box-sizing: border-box;
  }
  .tagline p {
    writing-mode: vertical-rl; margin: 0; font-weight: 900; font-size: 54px;
    line-height: 1.35; letter-spacing: 2px;
  }
  .tagline .tcy { text-combine-upright: all; }

  .title { position: absolute; left: 0; top: 530px; width: 752px; text-align: center; font-weight: 900; }
  .title .line1 { font-size: 82px; line-height: 1.1; letter-spacing: 2px; }
  .title .line2 { font-size: 86px; line-height: 1.1; }
  .title .line3 { font-size: 92px; line-height: 1.15; }
  .title .num {
    font-size: 128px; color: var(--accent);
    -webkit-text-stroke: 4px var(--ink); paint-order: stroke fill;
  }

  .bonus {
    position: absolute; left: 0; top: 860px; width: 752px; height: 340px;
    background: var(--white);
  }
  .bonus-head {
    text-align: center; font-weight: 700; font-size: 26px; line-height: 1.3;
    position: relative; margin: 18px auto 10px; width: 420px;
  }
  .bonus-head::before, .bonus-head::after {
    content: ""; position: absolute; top: 8px; width: 30px; height: 50px;
    border-top: 3px solid var(--ink);
  }
  .bonus-head::before { left: 0; border-left: 3px solid var(--ink); transform: skewX(-20deg); }
  .bonus-head::after { right: 0; border-right: 3px solid var(--ink); transform: skewX(20deg); }
  .bonus-list { list-style: none; margin: 0 24px; padding: 0; }
  .bonus-item {
    display: flex; align-items: center; height: 76px; border-bottom: 2px solid var(--line);
    font-weight: 700; font-size: 23px; line-height: 1.4;
  }
  .bonus-item:last-child { border-bottom: none; }
  .bonus-item .badge {
    flex: none; width: 52px; height: 52px; margin-right: 22px; background: var(--accent);
    display: flex; align-items: center; justify-content: center; font-size: 30px; font-weight: 900;
  }
  .bonus-item .big { font-size: 28px; }
</style>
</head>
<body>
<div class="cover">
  <div class="portrait p1" role="img" aria-label="笑顔の女性のイラスト"></div>
  <div class="portrait p2" role="img" aria-label="手を合わせて喜ぶ女性のイラスト"></div>
  <div class="portrait p3" role="img" aria-label="ひらめいた表情の女性のイラスト"></div>
  <div class="portrait p4" role="img" aria-label="眼鏡をかけた女性のイラスト"></div>
  <div class="portrait p5" role="img" aria-label="髪をまとめた女性のイラスト"></div>

  <div class="tagline">
    <p>毎月収入<br><span class="tcy">10</span>万円UPしたい<br>あなたに贈る！</p>
  </div>

  <h1 class="title" style="margin:0">
    <div class="line1">知っておくべき</div>
    <div class="line2">WEBテクニック</div>
    <div class="line3"><span class="num">77</span>のポイント</div>
  </h1>

  <section class="bonus">
    <div class="bonus-head">3つの特典プレゼントで<br>しっかりサポート！</div>
    <ul class="bonus-list">
      <li class="bonus-item"><span class="badge">1</span><span class="big">何が足りないかすぐ分かる！WEBチェックシート</span></li>
      <li class="bonus-item"><span class="badge">2</span><span>1年で1万人フォロワーを達成した<br>Plumoraフォロワー増やしのコツ</span></li>
      <li class="bonus-item"><span class="badge">3</span><span>最短で成功へ向かう無料コンサル</span></li>
    </ul>
  </section>
</div>
</body>
</html>
```